Torven Medical needs bold attention catching website for healthcare professionals(target)

I need a hero page as well as a products and about page for a website of mine. I specialize in orthopedic instruments . Specifically bone drills and saws. This whole company was founded to bring superb quality highly discounted medical instruments. Specifically bone drills, bone saws, k-wires and pins. Two main points should be cost savings and superior quality.

Target Market(s)

healthcare professionals Surgeons and hospital material managers

Number of Pages Required

3 page

Font styles to use
Serif

Colors

Designer to choose colors to be used in the design.

Requirements
Must have
• colors should match logo design

```html
<!DOCTYPE html>
<html lang="en">
<head>
<meta charset="utf-8">
<title>Torven Medical — Orthopedic Instruments</title>
<link rel="stylesheet" href="https://fonts.googleapis.com/css2?family=Merriweather:wght@400;700&family=Open+Sans:wght@400;600&display=swap">
<style>
:root{
  --orange:#f39325;
  --orange-dark:#e8851a;
  --slate:#4a5b66;
  --ink:#2b2b2b;
  --muted:#8a8a8a;
  --pale:#f6f7fb;
  --footer:#2a2a2a;
  --white:#ffffff;
}
*{margin:0;padding:0;box-sizing:border-box}
html,body{width:1200px;height:2625px;overflow:hidden;background:var(--white)}
body{font-family:"Open Sans",sans-serif;color:var(--ink);position:relative}
.serif{font-family:"Merriweather",serif}
.abs{position:absolute}

/* header */
.site-header{position:absolute;left:0;top:0;width:1200px;height:112px;background:var(--white)}
.brand{position:absolute;left:173px;top:38px;display:flex;align-items:center;gap:10px}
.brand-dot{width:22px;height:22px;border-radius:50%;background:var(--orange)}
.brand-name{font-family:"Merriweather",serif;font-size:21px;color:var(--ink);font-weight:400}
.main-nav{position:absolute;left:431px;top:48px;display:flex;gap:23px;font-family:"Merriweather",serif;font-size:12px;color:var(--ink)}
.main-nav .active{color:var(--orange)}
.caret{display:inline-block;width:5px;height:5px;border-right:1px solid var(--ink);border-bottom:1px solid var(--ink);transform:rotate(45deg);margin-left:5px;position:relative;top:-3px}
.search{position:absolute;left:863px;top:39px;width:143px;height:34px;border:1px solid #bdbdbd;border-radius:4px;font-family:"Merriweather",serif;font-size:11px;color:var(--muted);padding:10px 12px}
.search svg{position:absolute;right:11px;top:12px}

/* hero */
.hero{position:absolute;left:0;top:112px;width:1200px;height:456px;background:radial-gradient(ellipse at 60% 40%,#8a8a8a 0%,#6d6d6d 45%,#5a5a5a 100%)}
.hero-kicker{position:absolute;left:173px;top:116px;font-family:"Merriweather",serif;font-size:29px;color:var(--orange)}
.hero-title{position:absolute;left:173px;top:158px;font-family:"Merriweather",serif;font-weight:700;font-size:39px;color:var(--white)}
.hero-text{position:absolute;left:173px;top:218px;width:480px;font-size:12.5px;line-height:23px;color:var(--white)}
.btn{background:var(--orange);color:var(--white);border-radius:3px;display:flex;align-items:center;justify-content:center}
.hero-btn{position:absolute;left:173px;top:290px;width:173px;height:43px;font-size:12.5px}
.hero-arrow{position:absolute;top:216px}
.hero-product{position:absolute;left:790px;top:100px;width:165px;height:258px;background:linear-gradient(90deg,rgba(230,230,230,.35),rgba(255,255,255,.55),rgba(230,230,230,.35));border-radius:6px}
.badge{position:absolute;left:930px;top:70px;width:94px;height:94px;border-radius:50%;background:var(--orange);color:var(--white);text-align:center}
.badge .pct{display:block;font-size:25px;margin-top:14px;line-height:28px}
.badge .off{display:block;font-size:31px;font-weight:700;font-style:italic;line-height:32px}
.dots{position:absolute;display:flex;gap:12px}
.dot{width:11px;height:11px;border-radius:50%;background:var(--white)}
.dot.on{background:var(--orange)}

/* welcome */
.section-title{position:absolute;left:0;width:1200px;text-align:center;font-family:"Merriweather",serif;font-size:32px;color:var(--ink)}
.section-title .hl{color:var(--orange);font-weight:700}
.section-title b{font-weight:700}
.lead{position:absolute;text-align:center;font-size:12.5px;line-height:21px;color:var(--muted)}
.feature{position:absolute;top:805px;width:405px;height:228px;border-radius:4px;color:var(--white);text-align:center}
.feature.cost{left:173px;background:linear-gradient(135deg,#f5a040,#f08d1f)}
.feature.quality{left:601px;background:linear-gradient(135deg,#52646f,#44555f)}
.feature svg{margin-top:30px}
.feature h3{font-family:"Merriweather",serif;font-weight:700;font-size:19px;margin-top:16px}
.feature p{font-size:12.5px;line-height:21px;margin:18px auto 0;width:350px}

/* products */
.products{position:absolute;left:0;top:1123px;width:1200px;height:619px;background:var(--pale)}
.product{position:absolute;top:217px;width:263px}
.product .shot{height:160px;background:var(--white)}
.product .shot div{width:100%;height:100%;background:radial-gradient(ellipse at center,#d9dcdf 0%,#f2f3f4 55%,#ffffff 80%)}
.product .label{text-align:center;font-family:"Merriweather",serif;font-size:14px;margin-top:15px}
.promo{position:absolute;left:173px;top:468px;width:691px;height:62px;background:var(--slate);color:var(--white);font-family:"Merriweather",serif;font-size:14.5px;padding:20px 30px}
.promo u{font-style:italic;font-weight:700}
.promo-btn{position:absolute;left:884px;top:468px;width:120px;height:62px;font-family:"Merriweather",serif;font-size:14.5px;border-radius:0}

/* testimonials */
.testimonials{position:absolute;left:0;top:1742px;width:1200px;height:336px}
.t-left{position:absolute;left:0;top:0;width:650px;height:336px;background:linear-gradient(135deg,#f5a040,#ef8d22)}
.t-left h2{position:absolute;left:0;width:728px;top:126px;text-align:center;font-family:"Merriweather",serif;font-weight:400;font-size:33px;line-height:50px;color:var(--white)}
.t-left h2 b{font-weight:700}
.t-quote{position:absolute;left:672px;top:136px;width:335px;text-align:center;font-size:12.5px;line-height:21px;color:#6a6a6a}
.t-name{position:absolute;left:672px;top:218px;width:335px;text-align:center;font-family:"Merriweather",serif;font-size:14px;color:var(--orange)}
.sdot{width:7px;height:7px;border-radius:50%;background:#cfcfcf}
.sdot.on{background:var(--orange)}

/* assistance */
.assist{position:absolute;left:0;top:2078px;width:1200px;height:204px;background:var(--pale);text-align:center}
.assist h2{margin-top:69px;font-family:"Merriweather",serif;font-weight:400;font-size:20px;color:#4a4a4a}
.assist p{margin-top:10px;font-size:12.5px;color:#555}
.assist p a{font-family:"Merriweather",serif;font-size:17px;color:var(--orange);text-decoration:underline}

/* footer */
.site-footer{position:absolute;left:0;top:2282px;width:1200px;height:343px;background:linear-gradient(135deg,#2e2e2e,#242424 60%,#2c2c2c);color:var(--white)}
.footer-nav{position:absolute;left:0;top:56px;width:1200px;display:flex;justify-content:center;font-family:"Merriweather",serif;font-size:14px}
.footer-nav span{padding:0 22px}
.footer-nav .sep{padding:0;color:var(--orange)}
.f-col{position:absolute;top:128px}
.f-col h4{font-family:"Merriweather",serif;font-weight:400;font-size:20px;color:var(--orange);margin-bottom:18px}
.f-col li{list-style:none;font-size:11px;line-height:25.5px}
.f-col .k{color:var(--orange);font-weight:600}
.f-col svg{vertical-align:-1px;margin-right:5px}
.nl-input{width:193px;height:35px;background:var(--white);border-radius:3px;font-size:10px;color:#aaa;padding:11px 19px}
.nl-btn{width:97px;height:35px;font-size:11px;margin-top:12px}
.copyright{position:absolute;left:173px;top:312px;font-size:10px}
.legal{position:absolute;left:876px;top:312px;font-size:10px}
</style>
</head>
<body>

<header class="site-header">
  <div class="brand"><span class="brand-dot"></span><span class="brand-name">Torven Medical</span></div>
  <nav class="main-nav">
    <span class="active">Home</span><span>About Us</span><span>Products<i class="caret"></i></span><span>Pricing<i class="caret"></i></span><span>Contact Us</span>
  </nav>
  <div class="search">Search
    <svg width="9" height="9" viewBox="0 0 10 10"><circle cx="4" cy="4" r="3" fill="none" stroke="#555" stroke-width="1.3"/><line x1="6.3" y1="6.3" x2="9" y2="9" stroke="#555" stroke-width="1.3"/></svg>
  </div>
</header>

<section class="hero" role="img" aria-label="Greyscale photo of a surgeon examining a patient's shoulder">
  <div class="hero-kicker">High Quality</div>
  <h1 class="hero-title">Orthopedic Instruments</h1>
  <p class="hero-text">Welcome to our website! We are Torven Medical &amp; we are manufacturer of Orthopedic Instruments. We supply to over 80 countries.</p>
  <div class="btn hero-btn">Check Our Products&nbsp;&nbsp;<span style="font-size:11px">»</span></div>
  <svg class="hero-arrow" style="left:57px" width="16" height="26" viewBox="0 0 16 26"><polyline points="13,2 3,13 13,24" fill="none" stroke="#fff" stroke-width="3"/></svg>
  <svg class="hero-arrow" style="left:1124px" width="16" height="26" viewBox="0 0 16 26"><polyline points="3,2 13,13 3,24" fill="none" stroke="#fff" stroke-width="3"/></svg>
  <div class="hero-product" role="img" aria-label="Product photo of five orthopedic drill bits"></div>
  <div class="badge"><span class="pct">25%</span><span class="off">OFF</span></div>
  <div class="dots" style="left:572px;top:411px"><span class="dot"></span><span class="dot on"></span><span class="dot"></span></div>
</section>

<h2 class="section-title" style="top:649px">Welcome To <span class="hl">Torven</span> <b>MEDICAL</b></h2>
<p class="lead" style="left:245px;top:700px;width:710px">Lorem ipsum dolor sit amet, consectetur adipiscing elit, sed do eiusmod tempor incididunt ut labore et dolore magna aliqua. Ut enim ad minim veniam, quis nostrud exercitation ullamco laboris nisi ut aliquip ex ea commodo consequat. Duis aute irure dolor in reprehenderit in voluptate velit esse cillum dolore eu fugiat nulla pariatur.</p>

<div class="feature cost" role="img" aria-label="Orange tinted photo of a doctor with medical tools">
  <svg width="70" height="70" viewBox="0 0 70 70" fill="none" stroke="#fff" stroke-width="2"><rect x="6" y="10" width="40" height="48" rx="3"/><line x1="14" y1="22" x2="38" y2="22"/><line x1="14" y1="32" x2="32" y2="32"/><circle cx="50" cy="50" r="15" fill="#f39325"/><path d="M54 43c-2-2-8-2-8 2s8 2 8 6-6 4-8 2M50 40v20"/></svg>
  <h3>COST EFFECTIVE</h3>
  <p>Sed ut perspiciatis unde omnis iste natus error sit voluptatem accusantium doloremque laudantium, totam rem aperiam</p>
</div>
<div class="feature quality" role="img" aria-label="Slate tinted photo of surgical instruments">
  <svg width="70" height="70" viewBox="0 0 70 70" fill="none" stroke="#fff" stroke-width="2"><path d="M35 6l24 9v18c0 15-11 25-24 31C22 58 11 48 11 33V15z"/><polyline points="23,35 32,44 48,26"/></svg>
  <h3>SUPERIOR QUALITY</h3>
  <p>Sed ut perspiciatis unde omnis iste natus error sit voluptatem accusantium doloremque laudantium, totam rem aperiam</p>
</div>

<section class="products">
  <h2 class="section-title" style="top:82px">Our Top <span class="hl">Products</span></h2>
  <p class="lead" style="left:255px;top:134px;width:690px">Lorem ipsum dolor sit amet, consectetur adipiscing elit, sed do eiusmod tempor incididunt ut labore et dolore magna aliqua. Ut enim ad minim quisexercitation ullamco laboris nisi ut aliquip ex ea commodo consequat.</p>
  <svg class="abs" style="left:136px;top:285px" width="14" height="24" viewBox="0 0 14 24"><polyline points="12,2 3,12 12,22" fill="none" stroke="#f39325" stroke-width="2.5"/></svg>
  <svg class="abs" style="left:1028px;top:285px" width="14" height="24" viewBox="0 0 14 24"><polyline points="2,2 11,12 2,22" fill="none" stroke="#f39325" stroke-width="2.5"/></svg>
  <div class="product" style="left:173px"><div class="shot"><div role="img" aria-label="Product photo of a bone saw"></div></div><div class="label">Bone Saw</div></div>
  <div class="product" style="left:458px"><div class="shot"><div role="img" aria-label="Product photo of a bone drill"></div></div><div class="label">Bone Drill</div></div>
  <div class="product" style="left:743px"><div class="shot"><div role="img" aria-label="Product photo of two K-wires"></div></div><div class="label">K-Wires</div></div>
  <div class="promo">Flat <u>25%</u> discount on our latest products for all. Enjoy the weekend sale by Torven Medical</div>
  <div class="btn promo-btn">Shop Now</div>
</section>

<section class="testimonials">
  <div class="t-left" role="img" aria-label="Orange tinted photo of a doctor holding a clipboard">
    <h2>What clients say about<br><b>TORVEN MEDICAL</b></h2>
  </div>
  <svg class="abs" style="left:809px;top:68px" width="60" height="44" viewBox="0 0 60 44" fill="none" stroke="#f39325" stroke-width="2"><path d="M14 42a12 12 0 1 1 0-24c1-8 6-14 13-16M44 42a12 12 0 1 1 0-24c1-8 6-14 13-16"/></svg>
  <p class="t-quote">Lorem ipsum dolor sit amet, consectetur adipiscing elit, sed do eiusmod tempor incididunt ut labore et dolore magna aliqua. Ut enim ad minim quisexercitation ullamco.</p>
  <div class="t-name">R Whitfield</div>
  <div class="dots" style="left:818px;top:263px;gap:11px"><span class="sdot on"></span><span class="sdot"></span><span class="sdot"></span></div>
</section>

<section class="assist">
  <h2>Need any type of assistance related to our orthopedic instruments ?</h2>
  <p><svg width="10" height="10" viewBox="0 0 10 10"><path d="M2 1l2 2-1 1.5c.8 1.6 1.9 2.7 3.5 3.5L8 6l2 2-1.5 1.8C4.5 9.5.5 5.5.2 1.5z" fill="#f39325"/></svg> Call Us at <a>+123 555 01942</a></p>
</section>

<footer class="site-footer" role="img" aria-label="Dark background photo of medical equipment">
  <nav class="footer-nav">
    <span>Our Products</span><span class="sep">|</span><span>News &amp; Events</span><span class="sep">|</span><span>Become a Distributor</span><span class="sep">|</span><span>FAQ’s</span><span class="sep">|</span><span>Vendor Registartion</span>
  </nav>
  <div class="f-col" style="left:173px">
    <h4>Certificates</h4>
    <ul><li>ISO : 9001-2015</li><li>ISO 13485:2016</li><li>Quality Policy</li><li>WHO: GMP Compliance</li></ul>
  </div>
  <div class="f-col" style="left:387px">
    <h4>Get In Touch</h4>
    <ul>
      <li><svg width="10" height="10" viewBox="0 0 10 10"><path d="M5 1L1 4.5h1.2V9h2.3V6.5h1V9h2.3V4.5H9z" fill="#f39325"/></svg><span class="k">Address:</span> 48 Larkmoor Avenue, Fenwick City, United States of America (40219)</li>
      <li style="margin-top:6px"><svg width="10" height="10" viewBox="0 0 10 10"><path d="M2 1l2 2-1 1.5c.8 1.6 1.9 2.7 3.5 3.5L8 6l2 2-1.5 1.8C4.5 9.5.5 5.5.2 1.5z" fill="#f39325"/></svg><span class="k">Telephone:</span> +12-55-40918300 (100 lines)</li>
      <li style="margin-top:6px"><svg width="11" height="9" viewBox="0 0 11 9"><rect x=".5" y=".5" width="10" height="8" fill="none" stroke="#f39325"/><polyline points=".5,.5 5.5,5 10.5,.5" fill="none" stroke="#f39325"/></svg><span class="k">Email:</span> info@torvenmedical.com</li>
    </ul>
  </div>
  <div class="f-col" style="left:814px">
    <h4>Newsletter</h4>
    <div class="nl-input">Enter email here...</div>
    <div class="btn nl-btn">Subscribe</div>
  </div>
  <div class="copyright">Copyright © 2019 torvenmedical.com. All rights reserved.</div>
  <div class="legal">Disclaimer &nbsp;&nbsp;|&nbsp;&nbsp; Privacy Policy</div>
</footer>

</body>
</html>
```